Plakat für Fensterbau-Meisterbetrieb
Zielgruppe
Wir sind ein Fensterbau-Meisterbetrieb und überwiegend in der Modernisierung, Restaurierung und Instandhaltung tätig. Unsere Zielgruppe sind in unserer Region alle die Interesse an neuen Fenstern/Haustüren usw. haben.
Aufgabenstellung
Gesucht wird ein Design für ein Gerüst-Plakat, die Maße sind in den Anhängen. Das Design sollte an dem Bestehenden Firmenlogo/Website angeglichen sein. Ein kurzer Werbespruch 'Fenster die begeistern!' sollte auf dem Plakat zu finden sein. Die Homepage, Adresse (Am Wiesenrain 7, 74219 Lindenbach) und ganz Wichtig das Firmenlogo sollte ebenfalls vertreten sein.
Ansonsten lassen wir uns gerne von Kreativen Vorschlägen überraschen. =)
Ein Briefbogen zur Orientierung ist ebenfalls im Anhang.
Nachtrag zu den Vorgaben:
Das Firmenlogo sollte der „eyecatcher“ sein und der Werbespruch eher Nebensache.
Schriftart: MavenPro / MavenRegular

```html
<!DOCTYPE html>
<html lang="de">
<head>
<meta charset="utf-8">
<title>Plakat Kastellmann – Varianten</title>
<link href="https://fonts.googleapis.com/css2?family=Maven+Pro:wght@400;600;700&family=Roboto:wght@400&display=swap" rel="stylesheet">
<style>
  :root {
    --page: #ffffff;
    --ink: #575757;
    --green: #78b82a;
    --green-light: #9cc65a;
    --green-deep: #2f8a2a;
    --label: #111111;
  }
  * { margin: 0; padding: 0; box-sizing: border-box; }
  html, body { width: 1200px; height: 2483px; overflow: hidden; background: var(--page); }
  body { position: relative; font-family: "Maven Pro", sans-serif; color: var(--ink); }

  .poster {
    position: absolute; left: 133px; width: 979px; height: 1003px;
    background: #fff; overflow: hidden;
    box-shadow: 0 0 60px rgba(0,0,0,0.18);
  }
  .poster--a { top: 145px; }
  .poster--b { top: 1400px; }

  .variant-label {
    position: absolute; left: 0; width: 1200px; text-align: center;
    font-family: "Roboto", sans-serif; font-size: 44px; color: var(--label);
  }
  .variant-label--a { top: 1195px; }
  .variant-label--b { top: 2420px; }

  .brand {
    position: absolute; left: 0; width: 979px;
    display: flex; align-items: center; justify-content: center; gap: 26px;
    font-weight: 700; font-size: 96px; color: var(--ink); letter-spacing: 4px; line-height: 1;
  }
  .brand__square { width: 36px; height: 36px; background: var(--green); flex: none; }
  .poster--a .brand { top: 192px; }
  .poster--b .brand { top: 517px; }

  .contact { position: absolute; left: 0; width: 979px; text-align: center; line-height: 53px; }
  .contact__address { font-size: 44px; font-weight: 400; letter-spacing: 1px; }
  .contact__web { font-size: 45px; font-weight: 700; letter-spacing: 0.5px; }
  .poster--a .contact { top: 381px; }
  .poster--a .contact__web { color: var(--green); }

  .slogan { position: absolute; left: 83px; font-size: 43px; font-weight: 700; line-height: 49px; letter-spacing: 1px; }
  .poster--a .slogan { top: 586px; color: var(--ink); }
  .poster--b .slogan { top: 151px; color: var(--green); }

  .visual { position: absolute; left: 0; top: 0; }

  .contact-band {
    position: absolute; left: 0; bottom: 0; width: 979px; height: 285px;
    background: linear-gradient(180deg, var(--green) 0%, var(--green-light) 100%);
    color: #fff;
  }
  .contact-band .contact { top: 78px; }
</style>
</head>
<body>

<section class="poster poster--a">
  <div class="brand"><span class="brand__square"></span>Kastellmann</div>
  <div class="contact">
    <p class="contact__address">Am Wiesenrain 7, 74219 Lindenbach</p>
    <p class="contact__web">www.kastellmann-fenstertechnik.de</p>
  </div>
  <p class="slogan">Fenster,<br>die begeistern!</p>
  <svg class="visual" width="979" height="1003" viewBox="0 0 979 1003" role="img" aria-label="Foto einer grün verglasten Gebäudefassade in Dreiecksform">
    <defs>
      <linearGradient id="glassA" x1="0" y1="1" x2="1" y2="0">
        <stop offset="0" stop-color="#2f8a2a"/>
        <stop offset="0.5" stop-color="#7ab92e"/>
        <stop offset="1" stop-color="#e6f0d0"/>
      </linearGradient>
    </defs>
    <polygon points="182,1003 617,528 979,890 979,1003" fill="url(#glassA)"/>
  </svg>
</section>
<p class="variant-label variant-label--a">Variante A</p>

<section class="poster poster--b">
  <p class="slogan">Fenster,<br>die begeistern!</p>
  <svg class="visual" width="979" height="1003" viewBox="0 0 979 1003" role="img" aria-label="Foto einer grün verglasten Gebäudefassade in der oberen rechten Ecke">
    <defs>
      <linearGradient id="glassB" x1="0" y1="0" x2="1" y2="1">
        <stop offset="0" stop-color="#e6f0d0"/>
        <stop offset="0.5" stop-color="#8cc23e"/>
        <stop offset="1" stop-color="#2f8a2a"/>
      </linearGradient>
    </defs>
    <polygon points="690,0 979,0 979,595 512,157" fill="url(#glassB)"/>
  </svg>
  <div class="brand"><span class="brand__square"></span>Kastellmann</div>
  <div class="contact-band">
    <div class="contact">
      <p class="contact__address">Am Wiesenrain 7, 74219 Lindenbach</p>
      <p class="contact__web">www.kastellmann-fenstertechnik.de</p>
    </div>
  </div>
</section>
<p class="variant-label variant-label--b">Variante B</p>

</body>
</html>
```